Professional Label needed for Velvet Paw Biscuit Co

I make 100% organic dog treats. Wheat and gluten free.

I will be packaging them in a window kraft bag. I need a nicely designed label to place on each bag. The name of my company is The Velvet Paw Biscuit Company. All ingredients are organic and no preservatives are used. They are a healthy alternative to "assembly line" treats made by large companies.
Updates

Target Market(s)

Dog Owners

Industry/Entity Type

Pet

Font styles to use
Serif

Colors
00a990

Requirements
Must have
• can use a dog paw - see attached files. Dog themed, 100%
• Organic Dog Treats.
• No preservatives, nothing artificial, no corn, wheat or soy, made in Texas, USA with 100% organic ingredients. Non GMO
• Must have "dog treat" somewhere.
• "The Velvet Paw Biscuit Co." font size needs to be bigger than anything else.
Nice to have
• I like teal and brown
• I'm open to anything really as long as its dog themed

```html
<!DOCTYPE html>
<html lang="en">
<head>
<meta charset="utf-8">
<title>The Velvet Paw Biscuit Co. – Bag Label</title>
<link rel="stylesheet" href="https://fonts.googleapis.com/css2?family=Oswald:wght@400;500&family=Archivo+Narrow:wght@700&display=swap">
<style>
  :root {
    --canvas: #ffffff;
    --teal: #14a89b;
    --teal-deep: #0f897e;
    --mint-band: #e6f3ee;
    --mint: #86cfa6;
    --brown-strip: #4f3424;
    --brown-box: #6b4a35;
    --paw-brown: #7a4320;
    --paw-light: #93552c;
    --badge-green: #5bab5a;
    --white: #ffffff;
  }
  * { margin: 0; padding: 0; box-sizing: border-box; }
  html, body {
    width: 1200px;
    height: 1200px;
    overflow: hidden;
    background: var(--canvas);
  }
  .label {
    position: absolute;
    left: 100px;
    top: 100px;
    width: 1000px;
    height: 1000px;
    background: var(--teal);
    overflow: hidden;
  }
  .brand-strip {
    position: absolute;
    left: 0;
    top: 104px;
    width: 100%;
    height: 126px;
    background: var(--brown-strip);
  }
  .brand-plate {
    position: absolute;
    left: 114px;
    top: 57px;
    width: 770px;
    height: 244px;
    background: var(--brown-box);
    display: flex;
    flex-direction: column;
    align-items: center;
    justify-content: center;
    gap: 18px;
  }
  .brand-name {
    font-family: "Oswald", sans-serif;
    font-weight: 500;
    font-size: 66px;
    line-height: 1;
    color: var(--mint);
    white-space: nowrap;
  }
  .brand-phone {
    font-family: "Oswald", sans-serif;
    font-weight: 400;
    font-size: 24px;
    letter-spacing: 1px;
    color: var(--mint);
  }
  .title-band {
    position: absolute;
    left: 0;
    top: 417px;
    width: 100%;
    height: 164px;
    background: var(--mint-band);
  }
  .title-kicker {
    position: absolute;
    left: 40px;
    top: 440px;
    font-family: "Oswald", sans-serif;
    font-weight: 400;
    font-size: 37px;
    line-height: 1;
    letter-spacing: 7px;
    color: var(--teal);
  }
  .title-main {
    position: absolute;
    left: 40px;
    top: 490px;
    font-family: "Oswald", sans-serif;
    font-weight: 500;
    font-size: 62px;
    line-height: 1;
    letter-spacing: 5px;
    color: var(--teal);
  }
  .claims-band {
    position: absolute;
    left: 0;
    top: 581px;
    width: 100%;
    height: 118px;
    background: var(--teal-deep);
  }
  .claims {
    position: absolute;
    left: 40px;
    top: 587px;
    font-family: "Archivo Narrow", sans-serif;
    font-weight: 700;
    font-size: 27px;
    line-height: 36px;
    letter-spacing: 2px;
    color: var(--white);
  }
  .paw-art {
    position: absolute;
    left: 470px;
    top: 420px;
    width: 500px;
    height: 520px;
    border-radius: 36px;
    background: linear-gradient(160deg, var(--paw-light), var(--paw-brown));
  }
  .badges {
    position: absolute;
    left: 40px;
    top: 748px;
    display: flex;
    gap: 22px;
  }
  .badge {
    position: relative;
    width: 166px;
    height: 160px;
  }
  .badge-ring {
    position: absolute;
    left: 7px;
    top: 4px;
    width: 152px;
    height: 152px;
    border-radius: 50%;
    background: var(--white);
    border: 7px solid var(--teal);
    box-shadow: 0 0 0 4px var(--white);
  }
  .badge-top, .badge-bottom {
    position: absolute;
    left: 0;
    width: 100%;
    text-align: center;
    font-family: "Oswald", sans-serif;
    font-weight: 400;
    letter-spacing: 1.5px;
    color: var(--teal);
    line-height: 1;
  }
  .badge-top { top: 30px; font-size: 13px; }
  .badge-top.is-large { top: 24px; font-size: 20px; }
  .badge-bottom { bottom: 30px; font-size: 13px; }
  .badge-word {
    position: absolute;
    left: 0;
    top: 58px;
    width: 166px;
    height: 44px;
    background: var(--white);
    border: 3px solid var(--badge-green);
    border-radius: 4px;
    display: flex;
    align-items: center;
    justify-content: center;
    font-family: "Oswald", sans-serif;
    font-weight: 500;
    font-size: 30px;
    letter-spacing: 2px;
    color: var(--badge-green);
    line-height: 1;
  }
  .origin {
    position: absolute;
    left: 52px;
    top: 940px;
    font-family: "Archivo Narrow", sans-serif;
    font-weight: 700;
    font-size: 28px;
    letter-spacing: 2px;
    color: var(--white);
  }
</style>
</head>
<body>
  <main class="label">
    <div class="brand-strip"></div>
    <header class="brand-plate">
      <div class="brand-name">The Velvet Paw Biscuit Co.</div>
      <div class="brand-phone">512-408-3196</div>
    </header>

    <div class="title-band"></div>
    <p class="title-kicker">100% ORGANIC</p>
    <h1 class="title-main">DOG TREATS</h1>

    <div class="claims-band"></div>
    <p class="claims">No preservatives,<br>nothing artificial, no corn,<br>wheat or soy</p>

    <div class="paw-art" role="img" aria-label="Large brown dog paw print with a heart-shaped pad"></div>

    <div class="badges">
      <div class="badge">
        <div class="badge-ring"></div>
        <span class="badge-top">MADE WITH</span>
        <span class="badge-word">NON-GMO</span>
        <span class="badge-bottom">INGREDIENT</span>
      </div>
      <div class="badge">
        <div class="badge-ring"></div>
        <span class="badge-top is-large">100%</span>
        <span class="badge-word">ORGANIC</span>
        <span class="badge-bottom">NATURAL</span>
      </div>
    </div>

    <p class="origin">MADE IN TEXAS, USA</p>
  </main>
</body>
</html>
```